Brightmoor Paving Stationery Design COMMITTED PAY

We need you to design stationary for a new Business called Brightmoor Paving. We have already got the logo designed and it is attached. Obviously we're looking for a stationery set designed around the colours and style to match the logo.

Use generic name, address, phone, fax, email etc ... I will edit text to required details.

What we need:
- Business Card Design Double Sided (90 x 55m + Bleed 3mm+)
- A4 Letter head Design
- A4 Presentation Folder Design
- Invoice Header Approx 210 x 55mm (Include Logo & Images)

And whatever other bonuses you'd like to kick in associated with the package.

I've attached some images and I've got hundreds more. If you want something else in the way of images, let me know.

I look forward to your seeing your designs.
Updates

Thought I should just clarify the follwoing:

1. The Invoice Header is just a branding for the top of my accounting package form.  It is not contain any contact information or the like.  Just logo, some images and some of your creativity and flair to bring it together.
2. The business does synthetic grass (75% of the business), Wetpour Rubber Surfaces, Softfall Surfaces and Rubber Wood Mulch.  These are categories you might choose to somehow highlight on the letterhead.
3. Business Card reverse side should be used to highlight the categories using images provided.

Wow, I've had some really nice designs submitted thus far, but my concern is that I can't just have an awesome looking card.  I really feel that my card needs to either show or say what we do.  Please make sure your design either shows or says the following:

- Synthetic Grass
- Wetpour Rubber Surfaces
- Softfall Surfaces
- Rubber Wood Mulch
- Shade Structures
- Landscape Structures

Just another note, don't know if I mentioned it or not in the original brief, but I prefer the use of icons instead of text for phone, email, fax etc labels.

Industry/Entity Type

Business

Requirements
Must have
• - Provide full editable source files
- Provide letterhead in MS Word format as well
- All designs must be awesome, but also show or say what we do. This is very important to me. I want anyone to look at our letterhead, business card etc and know instantly what it is that we do.
- Super quick turnaround on handover. I need card files to the printer on Monday morning (that's my Monday at GMT+10)
Nice to have
• - Creative use of the logo for a little bit of wow
Should not have
• - not square, boxy or rigid ... Loosen up a bit!

```html
<!DOCTYPE html>
<html lang="en">
<head>
<meta charset="utf-8">
<title>Brightmoor Paving — Letterhead</title>
<link href="https://fonts.googleapis.com/css2?family=Exo+2:wght@400;600;700&family=Open+Sans:wght@400&display=swap" rel="stylesheet">
<style>
  :root {
    --backdrop: #9a9a9a;
    --paper: #ffffff;
    --brand-blue: #1b8fd6;
    --brand-green: #78b833;
    --accent-blue-soft: #b7dbf2;
    --accent-green-soft: #cfe8b4;
    --ink: #2f2f2f;
    --ink-soft: #4a4a4a;
  }
  * { box-sizing: border-box; margin: 0; padding: 0; }
  html, body {
    width: 1200px; height: 900px; overflow: hidden;
    background: var(--backdrop);
  }
  .letterhead {
    position: absolute; left: 300px; top: 26px;
    width: 600px; height: 848px;
    background: var(--paper);
    box-shadow: 0 6px 18px rgba(0,0,0,.25);
    font-family: "Open Sans", sans-serif;
    color: var(--ink);
    overflow: hidden;
  }
  .brand-accent {
    position: absolute; right: 0; top: 150px;
    width: 120px; height: 260px;
  }
  .masthead { position: absolute; left: 44px; top: 44px; width: 420px; }
  .company-name {
    display: flex; align-items: center; gap: 10px;
    font-family: "Exo 2", sans-serif; font-weight: 700;
    font-size: 30px; line-height: 1; color: var(--brand-blue);
    text-transform: uppercase; letter-spacing: .5px;
    white-space: nowrap;
  }
  .company-name .dot {
    width: 26px; height: 26px; border-radius: 50%;
    background: var(--brand-green); flex: none;
  }
  .services {
    margin-top: 10px;
    font-family: "Exo 2", sans-serif; font-weight: 600;
    font-size: 10.5px; line-height: 1.45;
  }
  .services .blue { color: var(--brand-blue); }
  .services .green { color: var(--brand-green); }
  .services .sep { color: var(--ink-soft); font-weight: 400; }
  .letter-body {
    position: absolute; left: 44px; top: 190px; width: 416px;
    font-size: 9px; line-height: 1.6; color: var(--ink-soft);
  }
  .letter-body .salutation { margin-bottom: 12px; color: var(--ink); }
  .letter-body p { margin-bottom: 14px; text-align: justify; }
  .footer {
    position: absolute; left: 44px; right: 44px; bottom: 40px;
    display: flex; justify-content: space-between; align-items: flex-end;
    font-family: "Exo 2", sans-serif; font-size: 10px; color: var(--ink);
  }
  .contact-list { list-style: none; line-height: 1.7; }
  .contact-list li { display: flex; align-items: center; gap: 6px; }
  .contact-list svg { width: 10px; height: 10px; flex: none; }
  .address { line-height: 1.7; }
</style>
</head>
<body>
  <main class="letterhead">
    <svg class="brand-accent" viewBox="0 0 120 260" role="img" aria-label="Brand mark decoration in blue and green">
      <defs>
        <linearGradient id="accentFill" x1="0" y1="0" x2="0.4" y2="1">
          <stop offset="0" stop-color="var(--accent-blue-soft)"/>
          <stop offset="1" stop-color="var(--accent-green-soft)"/>
        </linearGradient>
      </defs>
      <path d="M120 0 V260 C60 250 18 200 18 130 C18 60 60 10 120 0 Z" fill="url(#accentFill)"/>
    </svg>

    <header class="masthead">
      <div class="company-name"><span class="dot"></span>Brightmoor Paving</div>
      <div class="services">
        <div><span class="blue">Synthetic Grass</span> <span class="sep">|</span> <span class="green">Wetpour Rubber Surfaces</span> <span class="sep">|</span> <span class="blue">Softfall Surfaces</span></div>
        <div><span class="green">Rubber Wood Mulch</span> <span class="sep">|</span> <span class="blue">Shade Structures</span> <span class="sep">|</span> <span class="green">Landscape Structures</span></div>
      </div>
    </header>

    <section class="letter-body">
      <div class="salutation">Dear Client,</div>
      <p>Lorem ipsum dolor sit amet, consectetur adipisicing elit, sed do eiusmod tempor incididunt ut labore et dolore magna aliqua. Ut enim ad minim veniam, quis nostrud exercitation ullamco laboris nisi ut aliquip ex ea commodo consequat. Duis aute irure dolor in reprehenderit in voluptate velit esse cillum dolore eu fugiat nulla pariatur. Excepteur sint occaecat cupidatat non proident, sunt in culpa qui officia deserunt mollit anim id est laborum.</p>
      <p>Lorem ipsum dolor sit amet, consectetur adipisicing elit, sed do eiusmod tempor incididunt ut labore et dolore magna aliqua. Ut enim ad minim veniam, quis nostrud exercitation ullamco laboris nisi ut aliquip ex ea commodo consequat. Duis aute irure dolor in reprehenderit in voluptate velit esse cillum dolore eu fugiat nulla pariatur. Excepteur sint occaecat cupidatat non proident, sunt in culpa qui officia deserunt mollit anim id est laborum.</p>
      <p>Lorem ipsum dolor sit amet, consectetur adipisicing elit, sed do eiusmod tempor incididunt ut labore et dolore magna aliqua. Ut enim ad minim veniam, quis nostrud exercitation ullamco laboris nisi ut aliquip ex ea commodo consequat. Duis aute irure dolor in reprehenderit in voluptate velit esse cillum dolore eu fugiat nulla pariatur. Excepteur sint occaecat cupidatat non proident, sunt in culpa qui officia deserunt mollit anim id est laborum.</p>
      <p>Lorem ipsum dolor sit amet, consectetur adipisicing elit, sed do eiusmod tempor incididunt ut labore et dolore magna aliqua. Ut enim ad minim veniam, quis nostrud exercitation ullamco laboris nisi ut aliquip ex ea commodo consequat. Duis aute irure dolor in reprehenderit in voluptate velit esse cillum dolore eu fugiat nulla pariatur. Excepteur sint occaecat cupidatat non proident, sunt in culpa qui officia deserunt mollit anim id est laborum.</p>
      <p>Lorem ipsum dolor sit amet, consectetur adipisicing elit, sed do eiusmod tempor incididunt ut labore et dolore magna aliqua. Ut enim ad minim veniam, quis nostrud exercitation ullamco laboris nisi ut aliquip ex ea commodo consequat. Duis aute irure dolor in reprehenderit in voluptate velit esse cillum dolore eu fugiat nulla pariatur. Excepteur sint occaecat cupidatat non proident, sunt in culpa qui officia deserunt mollit anim id est laborum.</p>
    </section>

    <footer class="footer">
      <div class="address">
        <div>Harbourton, Eastvale, P.O. Box 0000</div>
        <div>Builder Licence #4407219</div>
      </div>
      <ul class="contact-list">
        <li><svg viewBox="0 0 10 10" aria-hidden="true"><path d="M2 1h2l1 2.5-1.3.8a5 5 0 0 0 2 2l.8-1.3L9 6v2a1 1 0 0 1-1 1A7 7 0 0 1 1 2a1 1 0 0 1 1-1z" fill="var(--brand-blue)"/></svg>+00 21 480 000</li>
        <li><svg viewBox="0 0 10 10" aria-hidden="true"><rect x="2.5" y="1" width="5" height="3" fill="var(--brand-blue)"/><rect x="1" y="4" width="8" height="3.5" rx=".8" fill="var(--brand-blue)"/><rect x="2.5" y="6.5" width="5" height="2.5" fill="var(--brand-blue)" stroke="#fff" stroke-width=".6"/></svg>+00 21 480 000</li>
      </ul>
      <ul class="contact-list">
        <li><svg viewBox="0 0 10 10" aria-hidden="true"><rect x=".5" y="2" width="9" height="6.5" rx=".8" fill="var(--brand-blue)"/><path d="M1 2.6 5 5.6 9 2.6" fill="none" stroke="#fff" stroke-width=".8"/></svg>info@BrightmoorPaving.com</li>
        <li><svg viewBox="0 0 10 10" aria-hidden="true"><circle cx="5" cy="5" r="4.2" fill="none" stroke="var(--brand-blue)" stroke-width="1"/><ellipse cx="5" cy="5" rx="1.8" ry="4.2" fill="none" stroke="var(--brand-blue)" stroke-width=".8"/><path d="M.8 5h8.4" stroke="var(--brand-blue)" stroke-width=".8"/></svg>www.BrightmoorPaving.com</li>
      </ul>
    </footer>
  </main>
</body>
</html>
```